4Orbit Blueprint- Logo & Design Work

THIS IS PHASE ONE. I have a stock trading strategy. I need a schematic that shows how it works. I have included sketches. I want the scheme to look like Exhibit A. I want the circles to look like gear shifts in Exhibit B. After this first step is done, we will move on to creating logo like Exhibit C, a second logo like Exhibit D and another Schematic like Exhibit E.

```html
<!DOCTYPE html>
<html lang="en">
<head>
<meta charset="utf-8">
<title>4Orbit Blueprint – Strategy Schematic</title>
<link href="https://fonts.googleapis.com/css2?family=Poppins:wght@600;800&display=swap" rel="stylesheet">
<style>
  :root{
    --white:#ffffff;
    --stage-grey:#bcbdc0;
    --frame-light:#cfcfcf;
    --frame-pale:#e4e4e5;
    --gear-silver:#eeeeef;
    --teal-a:#0f9e8f;
    --teal-b:#5cc47e;
    --blue-a:#1e4cc2;
    --blue-b:#3d9fe2;
    --purple-a:#7a2ed6;
    --purple-b:#b246d8;
    --magenta-a:#a8107c;
    --magenta-b:#e03fa8;
    --orange-a:#ff5e1a;
    --orange-b:#ffbd3a;
    --ink:#111111;
  }
  html,body{margin:0;padding:0;overflow:hidden;}
  body{width:1200px;height:400px;background:var(--white);position:relative;font-family:"Poppins",sans-serif;}
  .panel{position:absolute;top:0;height:400px;}
  .panel--mono{left:0;width:401px;background:var(--white);}
  .panel--colour{left:401px;width:396px;background:var(--stage-grey);}
  .panel--brand{left:797px;width:403px;background:var(--white);display:flex;align-items:center;justify-content:center;}
  .schematic{position:absolute;top:0;left:0;width:400px;height:400px;}
  .panel--colour .schematic{left:-4px;}
  .gear-label{font-family:"Poppins",sans-serif;font-weight:600;fill:var(--white);}
  .gear-figure{font-family:"Poppins",sans-serif;font-weight:800;fill:var(--white);}
  .hub-name{font-family:"Poppins",sans-serif;font-weight:800;fill:var(--ink);}
  .brand-lockup{display:flex;align-items:center;gap:10px;}
  .brand-dot{width:22px;height:22px;border-radius:50%;background:var(--blue-a);}
  .brand-name{font-family:"Poppins",sans-serif;font-weight:800;font-size:30px;color:var(--ink);letter-spacing:0.5px;}
</style>
</head>
<body>

<svg width="0" height="0" style="position:absolute">
  <defs>
    <symbol id="gear" viewBox="-44 -44 88 88" overflow="visible">
      <circle r="36"/>
      <rect x="-5" y="-43" width="10" height="12" rx="1"/>
      <rect x="-5" y="-43" width="10" height="12" rx="1" transform="rotate(30)"/>
      <rect x="-5" y="-43" width="10" height="12" rx="1" transform="rotate(60)"/>
      <rect x="-5" y="-43" width="10" height="12" rx="1" transform="rotate(90)"/>
      <rect x="-5" y="-43" width="10" height="12" rx="1" transform="rotate(120)"/>
      <rect x="-5" y="-43" width="10" height="12" rx="1" transform="rotate(150)"/>
      <rect x="-5" y="-43" width="10" height="12" rx="1" transform="rotate(180)"/>
      <rect x="-5" y="-43" width="10" height="12" rx="1" transform="rotate(210)"/>
      <rect x="-5" y="-43" width="10" height="12" rx="1" transform="rotate(240)"/>
      <rect x="-5" y="-43" width="10" height="12" rx="1" transform="rotate(270)"/>
      <rect x="-5" y="-43" width="10" height="12" rx="1" transform="rotate(300)"/>
      <rect x="-5" y="-43" width="10" height="12" rx="1" transform="rotate(330)"/>
    </symbol>
    <linearGradient id="tealFill" x1="0" y1="1" x2="1" y2="0">
      <stop offset="0" stop-color="var(--teal-a)"/><stop offset="1" stop-color="var(--teal-b)"/>
    </linearGradient>
    <linearGradient id="tealArm" gradientUnits="userSpaceOnUse" x1="100" y1="300" x2="300" y2="100">
      <stop offset="0" stop-color="var(--teal-a)"/><stop offset="1" stop-color="var(--teal-b)"/>
    </linearGradient>
    <linearGradient id="blueFill" x1="0" y1="1" x2="1" y2="0">
      <stop offset="0" stop-color="var(--blue-a)"/><stop offset="1" stop-color="var(--blue-b)"/>
    </linearGradient>
    <linearGradient id="purpleFill" x1="0" y1="1" x2="1" y2="0">
      <stop offset="0" stop-color="var(--purple-a)"/><stop offset="1" stop-color="var(--purple-b)"/>
    </linearGradient>
    <linearGradient id="magentaFill" x1="0" y1="1" x2="1" y2="0">
      <stop offset="0" stop-color="var(--magenta-a)"/><stop offset="1" stop-color="var(--magenta-b)"/>
    </linearGradient>
    <linearGradient id="orangeFill" x1="0" y1="1" x2="1" y2="0">
      <stop offset="0" stop-color="var(--orange-a)"/><stop offset="1" stop-color="var(--orange-b)"/>
    </linearGradient>
    <filter id="gearShadow" x="-20%" y="-20%" width="140%" height="140%">
      <feDropShadow dx="1" dy="2" stdDeviation="2" flood-color="#000" flood-opacity="0.25"/>
    </filter>

    <g id="contentRebalance">
      <g stroke="#fff" stroke-width="1.3" fill="none">
        <line x1="-9" y1="-22" x2="9" y2="-22"/><circle cx="-4" cy="-22" r="2.2" fill="currentColor"/>
        <line x1="-9" y1="-16" x2="9" y2="-16"/><circle cx="3" cy="-16" r="2.2" fill="currentColor"/>
        <line x1="-9" y1="-10" x2="9" y2="-10"/><circle cx="0" cy="-10" r="2.2" fill="currentColor"/>
      </g>
      <text class="gear-label" x="0" y="5" font-size="7" text-anchor="middle">Rebalance</text>
      <text class="gear-label" x="0" y="13" font-size="7" text-anchor="middle">Annually</text>
    </g>
    <g id="contentTrend">
      <path d="M-22 12 V2 H-17 V-6 H-12 V-14" stroke="#fff" stroke-width="1.4" fill="none"/>
      <path d="M-14 -12 L-12 -16 L-10 -12" stroke="#fff" stroke-width="1.2" fill="none"/>
      <text class="gear-label" x="-6" y="-8" font-size="6.5">Trend</text>
      <text class="gear-figure" x="-6" y="7" font-size="15">33%</text>
      <text class="gear-label" x="-6" y="14" font-size="5.5">Allocation</text>
    </g>
    <g id="contentBuyHold">
      <text class="gear-label" x="-8" y="-8" font-size="6.5">Buy &amp; Hold</text>
      <text class="gear-figure" x="-8" y="7" font-size="15">33%</text>
      <text class="gear-label" x="-8" y="14" font-size="5.5">Allocation</text>
    </g>
    <g id="contentTactical">
      <text class="gear-label" x="-6" y="-8" font-size="6.5">Tactical</text>
      <text class="gear-figure" x="-6" y="7" font-size="15">33%</text>
      <text class="gear-label" x="-6" y="14" font-size="5.5">Allocation</text>
    </g>
    <g id="contentHub">
      <circle cx="-26" cy="-2" r="4" fill="var(--blue-a)"/>
      <text class="hub-name" x="4" y="-3" font-size="10" text-anchor="middle">4Orbit</text>
      <text class="hub-name" x="0" y="9" font-size="10" text-anchor="middle">Blueprint</text>
    </g>
  </defs>
</svg>

<section class="panel panel--mono">
  <svg class="schematic" viewBox="0 0 400 400" aria-label="Strategy schematic, teal version">
    <rect class="frame" x="77" y="74" width="248" height="249" fill="none" stroke="var(--frame-light)" stroke-width="8"/>
    <g class="arms" stroke="url(#tealArm)" stroke-width="26" fill="none">
      <path d="M109 109 Q170 150 201 199 Q232 248 293 289"/>
      <path d="M293 109 Q232 150 201 199 Q170 248 109 289"/>
    </g>
    <g class="gear gear--rebalance" transform="translate(109 109)">
      <use href="#gear" x="-44" y="-44" width="88" height="88" fill="url(#tealFill)"/>
      <circle r="31" fill="url(#tealFill)" stroke="#fff" stroke-width="2.5"/>
      <use href="#contentRebalance" color="url(#tealFill)" style="color:var(--teal-a)"/>
    </g>
    <g class="gear gear--trend" transform="translate(293 109)">
      <use href="#gear" x="-44" y="-44" width="88" height="88" fill="url(#tealFill)"/>
      <circle r="31" fill="url(#tealFill)" stroke="#fff" stroke-width="2.5"/>
      <use href="#contentTrend"/>
    </g>
    <g class="gear gear--buyhold" transform="translate(109 289)">
      <use href="#gear" x="-44" y="-44" width="88" height="88" fill="url(#tealFill)"/>
      <circle r="31" fill="url(#tealFill)" stroke="#fff" stroke-width="2.5"/>
      <use href="#contentBuyHold"/>
    </g>
    <g class="gear gear--tactical" transform="translate(293 289)">
      <use href="#gear" x="-44" y="-44" width="88" height="88" fill="url(#tealFill)"/>
      <circle r="31" fill="url(#tealFill)" stroke="#fff" stroke-width="2.5"/>
      <use href="#contentTactical"/>
    </g>
    <g class="gear gear--hub" transform="translate(201 199)">
      <use href="#gear" x="-53" y="-53" width="106" height="106" fill="url(#tealFill)"/>
      <circle r="38" fill="url(#tealFill)" stroke="#fff" stroke-width="2.5"/>
      <use href="#contentHub"/>
    </g>
  </svg>
</section>

<section class="panel panel--colour">
  <svg class="schematic" viewBox="0 0 400 400" aria-label="Strategy schematic, colour version">
    <rect class="frame" x="77" y="74" width="248" height="249" fill="none" stroke="var(--frame-pale)" stroke-width="8"/>
    <g class="arms" stroke-width="26" fill="none">
      <path d="M109 109 Q170 150 201 199" stroke="url(#blueFill)"/>
      <path d="M293 109 Q232 150 201 199" stroke="url(#purpleFill)"/>
      <path d="M109 289 Q170 248 201 199" stroke="url(#magentaFill)"/>
      <path d="M293 289 Q232 248 201 199" stroke="url(#orangeFill)"/>
    </g>
    <g class="gear gear--rebalance" transform="translate(109 109)">
      <use href="#gear" x="-44" y="-44" width="88" height="88" fill="var(--gear-silver)" filter="url(#gearShadow)"/>
      <circle r="31" fill="url(#blueFill)" stroke="#fff" stroke-width="2.5"/>
      <use href="#contentRebalance" style="color:var(--blue-a)"/>
    </g>
    <g class="gear gear--trend" transform="translate(293 109)">
      <use href="#gear" x="-44" y="-44" width="88" height="88" fill="var(--gear-silver)" filter="url(#gearShadow)"/>
      <circle r="31" fill="url(#purpleFill)" stroke="#fff" stroke-width="2.5"/>
      <use href="#contentTrend"/>
    </g>
    <g class="gear gear--buyhold" transform="translate(109 289)">
      <use href="#gear" x="-44" y="-44" width="88" height="88" fill="var(--gear-silver)" filter="url(#gearShadow)"/>
      <circle r="31" fill="url(#magentaFill)" stroke="#fff" stroke-width="2.5"/>
      <use href="#contentBuyHold"/>
    </g>
    <g class="gear gear--tactical" transform="translate(293 289)">
      <use href="#gear" x="-44" y="-44" width="88" height="88" fill="var(--gear-silver)" filter="url(#gearShadow)"/>
      <circle r="31" fill="url(#orangeFill)" stroke="#fff" stroke-width="2.5"/>
      <use href="#contentTactical"/>
    </g>
    <g class="gear gear--hub" transform="translate(201 199)">
      <use href="#gear" x="-53" y="-53" width="106" height="106" fill="var(--gear-silver)" filter="url(#gearShadow)"/>
      <circle r="38" fill="url(#tealFill)" stroke="#fff" stroke-width="2.5"/>
      <use href="#contentHub"/>
    </g>
  </svg>
</section>

<section class="panel panel--brand">
  <div class="brand-lockup">
    <span class="brand-dot"></span>
    <span class="brand-name">4Orbit Blueprint</span>
  </div>
</section>

</body>
</html>
```